Business Card for Musician

The company is called Tolvik Music Entertainment and i am the director (Priya Hallorin) . I would like a logo made along with a list of services i provide :

Rock Pop and Jazz Covers music for Weddings , Birthdays , Pubs, Bars and Restaurants

I provide Solo/Duo and Bands for these functions.

Another aspect is i teach guitar and do music workshops and compose music for television.

I want to go for something different than a photo of a guitar or singer..i like the idea of soundwaves and an ear. or ripples of sound like a music note (as a drop of water) and the sound rippling out..another idea is something with lighting (music lights) with different colours lighting up the name Tolvik..however im open to any ideas. Thanks

Target Market(s)

General Public, Music Agents, Venue Owners. English Speaking..adults from 25-50

Industry/Entity Type

Business

Font styles to use
Sans Serif

Colors

Designer to choose colors to be used in the design.

Requirements
Must have
• All the points about what i do...
Nice to have
• Logo could emphasize the TOL in Tolvik...
Should not have
• Not too busy please...Simple but gets the message across. NOthing obvious like a photo of a musician playing.

```html
<!DOCTYPE html>
<html lang="en">
<head>
<meta charset="utf-8">
<title>Tolvik Music Entertainment – Business Card</title>
<link rel="stylesheet" href="https://fonts.googleapis.com/css2?family=Lato:ital,wght@0,400;0,700;0,900;1,900&display=swap">
<style>
  :root {
    --card-bg: #0b0b0b;
    --text-white: #ffffff;
    --accent-green: #66ff00;
    --accent-red: #ec3a1c;
    --font-main: "Lato", sans-serif;
  }
  html, body {
    margin: 0;
    padding: 0;
    width: 1200px;
    height: 695px;
    overflow: hidden;
    background: var(--card-bg);
  }
  .card {
    position: relative;
    width: 1200px;
    height: 695px;
    background: var(--card-bg);
    font-family: var(--font-main);
    color: var(--text-white);
  }
  .brand-name {
    position: absolute;
    left: 115px;
    width: 945px;
    top: 70px;
    margin: 0;
    text-align: center;
    font-size: 170px;
    font-weight: 900;
    line-height: 220px;
    letter-spacing: 4px;
    color: var(--text-white);
  }
  .brand-tag {
    position: absolute;
    right: 162px;
    top: 280px;
    margin: 0;
    font-size: 58px;
    font-weight: 900;
    font-style: italic;
    line-height: 70px;
    color: var(--accent-green);
  }
  .director-name {
    position: absolute;
    left: 0;
    width: 1196px;
    top: 355px;
    margin: 0;
    text-align: center;
    font-size: 48px;
    font-weight: 900;
    line-height: 64px;
  }
  .services {
    position: absolute;
    left: 0;
    width: 1166px;
    top: 463px;
    margin: 0;
    padding: 0;
    list-style: none;
    text-align: center;
    font-size: 27px;
    font-weight: 400;
    line-height: 39px;
  }
  .services li::before {
    content: "";
    display: inline-block;
    width: 18px;
    height: 15px;
    margin-right: 12px;
    border-radius: 50%;
    background: var(--accent-green);
    vertical-align: 2px;
  }
  .contact {
    position: absolute;
    left: 0;
    width: 1190px;
    top: 608px;
    margin: 0;
    text-align: center;
    font-size: 25px;
    font-weight: 400;
    line-height: 34px;
  }
  .contact-label {
    color: var(--accent-red);
  }
</style>
</head>
<body>
  <main class="card">
    <h1 class="brand-name">Tolvik</h1>
    <p class="brand-tag">Music</p>
    <h2 class="director-name">Priya Hallorin</h2>
    <ul class="services">
      <li>Solo Artist, Duo &amp; Full Band</li>
      <li>Acoustic Tunes &amp; Smooth Jazz to Upbeat Rock &amp; Pop Covers</li>
      <li>Guitar Lessons, Workshops &amp; Session Playing</li>
    </ul>
    <p class="contact"><span class="contact-label">m</span> 0412 555 308 <span class="contact-label">e</span> tolvikmusicentertainment@mailpost.net</p>
  </main>
</body>
</html>
```